Cedarline Joinery eye catching business card

I need an eye catching business card that reflects my traditional, fun, handmade woodcraft shop. I make high end custom furniture and fine woodworking products, a lot of which are rustic, natural looking. We are a small shop but we produce awesome, one of a kind wood products, and our business card should reflect that. Our target audience is young professionals to retired folks who want a quality, local, handmade product. I'd like the Shop Nearby logo somewhere on the card, BUT not overwhelming, the main focus is my Logo, no preference on color whichever looks the best. Visit my website to get a feel for my company. Cedarlinejoinery.com
Target Market(s)
young professionals to retired folks. Any one who wants to furnish their home with quality handcrafted products.
Industry/Entity Type
Business
Contact Information for Business Card
Marlo Finch (555)417-6382
marlo@cedarlinejoinery.com
www.cedarlinejoinery.com
Look and feel

```html
<!DOCTYPE html>
<html lang="en">
<head>
<meta charset="utf-8">
<title>Cedarline Joinery — Business Card</title>
<link rel="stylesheet" href="https://fonts.googleapis.com/css2?family=Cinzel:wght@400&family=Montserrat:wght@300&display=swap">
<style>
  :root {
    --page: #ffffff;
    --stage: #eef0f0;
    --card-olive: #a89c6d;
    --card-ink: #ffffff;
    --wood-light: #a38e72;
    --wood-mid: #7d6a52;
    --wood-dark: #5a4b3a;
    --card-shadow: rgba(40, 36, 28, 0.18);
  }
  html, body {
    margin: 0;
    padding: 0;
    overflow: hidden;
  }
  body {
    width: 1200px;
    height: 1000px;
    background: var(--page);
    position: relative;
  }
  .stage {
    position: absolute;
    left: 0;
    top: 100px;
    width: 1200px;
    height: 800px;
    background: var(--stage);
  }
  .card {
    position: absolute;
    width: 560px;
    height: 320px;
    box-shadow: 0 6px 18px var(--card-shadow);
    box-sizing: border-box;
  }
  .card--contact {
    left: 280px;
    top: 70px;
    background: var(--card-olive);
    color: var(--card-ink);
    display: flex;
    flex-direction: column;
    align-items: center;
    justify-content: center;
    text-align: center;
  }
  .card__name {
    font-family: "Cinzel", serif;
    font-size: 30px;
    letter-spacing: 2px;
    margin: 0 0 14px;
    font-weight: 400;
  }
  .card__web,
  .card__details {
    font-family: "Montserrat", sans-serif;
    font-weight: 300;
    font-size: 12px;
    letter-spacing: 1.5px;
    text-transform: uppercase;
    margin: 0;
  }
  .card__details {
    margin-top: 34px;
  }
  .card__details span + span::before {
    content: "|";
    margin: 0 8px;
  }
  .card--brand {
    left: 360px;
    top: 420px;
    overflow: hidden;
  }
  .wood-grain {
    position: absolute;
    inset: 0;
    background:
      linear-gradient(178deg, rgba(255,255,255,0.06), rgba(0,0,0,0.12)),
      linear-gradient(90deg, var(--wood-mid), var(--wood-light) 35%, var(--wood-mid) 60%, var(--wood-dark));
  }
  .brand-mark {
    position: absolute;
    inset: 0;
    display: flex;
    align-items: center;
    justify-content: center;
  }
  .brand-mark__name {
    font-family: "Cinzel", serif;
    font-weight: 400;
    font-size: 40px;
    letter-spacing: 3px;
    color: var(--card-ink);
    margin: 0;
  }
</style>
</head>
<body>
  <main class="stage">
    <section class="card card--contact" aria-label="Business card, contact side">
      <h1 class="card__name">CEDARLINE JOINERY</h1>
      <p class="card__web">www.cedarlinejoinery.com</p>
      <p class="card__details">
        <span>Marlo Finch</span><span>marlo@cedarlinejoinery.com</span><span>(555)417-6382</span>
      </p>
    </section>

    <section class="card card--brand" aria-label="Business card, brand side">
      <div class="wood-grain" role="img" aria-label="Weathered knotty wood plank texture"></div>
      <div class="brand-mark">
        <p class="brand-mark__name">CEDARLINE JOINERY</p>
      </div>
    </section>
  </main>
</body>
</html>
```